Business Card Design

I would like a new business card design for an accounting firm that specializes in resolving clients tax problems. I want the card to give the impression that we are not your typical stodgy accounting firm, but at the same time we will get the job done.
Industry/Entity Type
Business
Contact Information for Business Card
Dorian T Welsby
Certified Public Accountant
38-27 52nd Street
Sunnyside, NY 11287
Tel: (718) 555-0142
Fax: (888) 555-0199
e-mail: dtwthecpa@ledgerpost.com
website: harborfilingreliefexperts.com

```html
<!DOCTYPE html>
<html lang="en">
<head>
<meta charset="utf-8">
<title>Dorian T Welsby — Business Card</title>
<link rel="stylesheet" href="https://fonts.googleapis.com/css2?family=Lato:wght@400;700&display=swap">
<style>
  :root {
    --page: #eeeeee;
    --card: #ffffff;
    --ink: #111111;
    --frame: #3a3a3a;
    --divider: #f1f1f1;
    --stop-red: #ee7b80;
    --check-blue: #d9e8f2;
    --skin: #f9d9b8;
  }
  * { margin: 0; padding: 0; box-sizing: border-box; }
  html, body { width: 1200px; height: 1200px; overflow: hidden; }
  body {
    background: var(--page);
    font-family: "Lato", sans-serif;
    color: var(--ink);
    position: relative;
  }
  .card {
    position: absolute;
    left: 40px; top: 271px;
    width: 1120px; height: 658px;
    background: var(--card);
    border: 3px solid var(--frame);
    box-shadow: 0 3px 8px rgba(0,0,0,.25);
  }
  .card__divider {
    position: absolute;
    left: 589px; top: 20px; bottom: 100px;
    width: 1px; background: var(--divider);
  }
  .identity { position: absolute; left: 0; width: 589px; top: 170px; text-align: center; }
  .identity__name { font-weight: 700; font-size: 48px; letter-spacing: .3px; }
  .identity__title { font-weight: 400; font-size: 37px; margin-top: 22px; }
  .contacts { position: absolute; left: 54px; top: 463px; list-style: none; }
  .contacts__item {
    display: flex; align-items: center;
    font-size: 34px; line-height: 41.5px; height: 41.5px;
  }
  .contacts__icon { width: 32px; height: 32px; margin-right: 14px; flex: none; }
  .illustration {
    position: absolute; left: 623px; top: 53px;
    width: 490px; height: 490px; border-radius: 50%;
    background: radial-gradient(circle at 55% 45%, var(--skin) 0%, var(--check-blue) 40%, var(--stop-red) 78%, #f4a3a6 100%);
    opacity: .9;
  }
  .address { position: absolute; left: 688px; top: 540px; font-size: 37px; line-height: 46px; }
  .address__line { display: flex; align-items: center; }
  .address__pin { width: 30px; height: 36px; margin-right: 8px; }
  .address__line--indent { padding-left: 38px; }
</style>
</head>
<body>
  <article class="card">
    <div class="card__divider"></div>

    <header class="identity">
      <h1 class="identity__name">Dorian T Welsby</h1>
      <p class="identity__title">Certified Public Accountant</p>
    </header>

    <ul class="contacts">
      <li class="contacts__item">
        <svg class="contacts__icon" viewBox="0 0 24 24"><path fill="#111" d="M6.6 2.5l3 3.5-1.8 2.4c1.2 2.6 3.3 4.8 6 6.1l2.4-1.8 3.5 3-1.6 3.6c-.4.6-1.2.9-2 .7C9.4 18.3 4.9 13.6 3.3 7.5c-.2-.8.1-1.6.8-2z"/></svg>
        (718) 555-0142
      </li>
      <li class="contacts__item">
        <svg class="contacts__icon" viewBox="0 0 24 24"><path fill="#111" d="M7 2h8l2 2v5H7zM3 10h18v8h-3v-3H6v3H3zM7 16h10v6H7z"/><rect x="17" y="11.5" width="2" height="1.5" fill="#fff"/></svg>
        (888) 555-0199
      </li>
      <li class="contacts__item">
        <svg class="contacts__icon" viewBox="0 0 24 24"><rect x="2" y="5" width="20" height="14" fill="none" stroke="#111" stroke-width="1.5"/><path d="M2 5l10 8 10-8M2 19l7.5-7M22 19l-7.5-7" fill="none" stroke="#111" stroke-width="1.5"/></svg>
        dtwthecpa@ledgerpost.com
      </li>
      <li class="contacts__item">
        <svg class="contacts__icon" viewBox="0 0 24 24"><g fill="none" stroke="#111" stroke-width="1.3"><circle cx="12" cy="12" r="10"/><ellipse cx="12" cy="12" rx="4.5" ry="10"/><path d="M2 12h20M4 6.5h16M4 17.5h16M12 2v20"/></g></svg>
        harborfilingreliefexperts.com
      </li>
    </ul>

    <div class="illustration" role="img" aria-label="Illustration: red prohibition sign over a hand signing a tax payment check"></div>

    <address class="address" style="font-style:normal">
      <div class="address__line">
        <svg class="address__pin" viewBox="0 0 20 24"><path fill="#111" d="M10 0C4.5 0 1 4 1 8.8 1 15 10 24 10 24s9-9 9-15.2C19 4 15.5 0 10 0zm0 12.5a3.8 3.8 0 110-7.6 3.8 3.8 0 010 7.6z"/></svg>
        38-27 52nd Street
      </div>
      <div class="address__line address__line--indent">Sunnyside, NY 11287</div>
    </address>
  </article>
</body>
</html>
```